Packaging Design for Makeup Remover Pads - The winner will do several follow-up products with us

We are building a new brand (Ecological, Young, Friendly, Sustainable, High Quality). We are starting with Makeup Remover Pads. Once the product is launched, other products will follow. We would love to find a designer who does all follow-up designs for us. Our product contains 24 pads with 70% bamboo and 30% cotton. It has 3 layers as a highlight and a free washing bag made of 100% cotton. We would be really happy with a modern, high-quality design. You do not have to invent everything new. Please read the enclosed project description (.pdf file)

Target Market(s)

Women who think sustainably and ecologically

Logo Text

BRIMO TALVE

Colors

Designer to choose colors to be used in the design.

Requirements
Must have
• Our product is% 26quot; premium% 26quot ;. This should be written on the packaging and by a top design. 2 layers of cotton / bamboo. We have 3 layers in top quality. Our package contains 24 pieces, which is more than comparable products have. The whole design should immediately show the customer that it is a sustainable product. It would be great if the logo% 26quot; BRIMO TALVE% 26quot; what a combined word-picture logo. Our first idea is holding hands, or hugging, or holding hands in their hands or holding hands on the earth, or .... This is just to give you a rough idea. Feel free to come up with your own ideas.
Nice to have
• We uploaded a product with a cute panda on the package. An eye-catcher of that kind would be fabulous.

```html
<!DOCTYPE html>
<html lang="en">
<head>
<meta charset="UTF-8">
<title>Brimo Talve – Reusable Cleaning Pads</title>
<link href="https://fonts.googleapis.com/css2?family=Poppins:ital,wght@0,400;0,500;0,700;1,400&display=swap" rel="stylesheet">
<style>
  :root {
    --kraft: #f0bb8b;
    --leaf-green: #2f6a10;
    --bamboo-tint: rgba(95, 125, 40, 0.22);
    --cream: #f6ecd9;
    --ink: #2a2a1f;
    --white: #ffffff;
  }
  html, body {
    margin: 0;
    padding: 0;
    overflow: hidden;
    background: var(--kraft);
  }
  .package-front {
    position: relative;
    width: 691px;
    height: 1200px;
    background: var(--kraft);
    font-family: "Poppins", sans-serif;
    overflow: hidden;
  }
  .bamboo-right, .bamboo-left {
    position: absolute;
  }
  .bamboo-right {
    right: 0;
    top: 0;
    width: 130px;
    height: 600px;
    background: linear-gradient(270deg, var(--bamboo-tint), rgba(95,125,40,0));
  }
  .bamboo-left {
    left: 0;
    top: 780px;
    width: 170px;
    height: 420px;
    background: linear-gradient(90deg, var(--bamboo-tint), rgba(95,125,40,0));
  }
  .brand-block {
    position: absolute;
    left: 237px;
    top: 258px;
    width: 219px;
    height: 133px;
    border-radius: 18px;
    background: var(--leaf-green);
    display: flex;
    align-items: center;
    justify-content: center;
  }
  .brand-name {
    color: var(--cream);
    font-weight: 500;
    font-size: 34px;
    line-height: 1.1;
    text-align: center;
    letter-spacing: 1px;
  }
  .product-title {
    position: absolute;
    left: 0;
    width: 691px;
    text-align: center;
    color: var(--leaf-green);
    font-weight: 700;
    margin: 0;
    white-space: nowrap;
  }
  .product-title.main { top: 436px; font-size: 62px; letter-spacing: 1px; }
  .product-title.sub { top: 512px; font-size: 39px; font-weight: 500; letter-spacing: 1px; }
  .content-box {
    position: absolute;
    left: 131px;
    top: 592px;
    width: 434px;
    height: 163px;
    border: 2px solid var(--white);
    box-sizing: border-box;
  }
  .mesh-bag {
    position: absolute;
    left: 50px;
    top: 14px;
    width: 74px;
    height: 93px;
    border-radius: 30px 30px 24px 24px;
    background: var(--leaf-green);
    opacity: 0.85;
  }
  .content-list {
    position: absolute;
    left: 136px;
    top: 30px;
    margin: 0;
    padding: 0;
    list-style: none;
    font-style: italic;
    font-size: 28px;
    line-height: 40px;
    color: var(--ink);
    white-space: nowrap;
  }
  .content-list .wide { margin-left: -90px; }
  .count-badge {
    position: absolute;
    left: 512px;
    top: 540px;
    width: 104px;
    height: 104px;
  }
  .benefits {
    position: absolute;
    top: 796px;
    left: 0;
    width: 691px;
  }
  .benefit {
    position: absolute;
    width: 200px;
    text-align: center;
    font-size: 26px;
    color: var(--ink);
    white-space: nowrap;
  }
  .benefit svg { display: block; margin: 0 auto 10px; }
  .benefit.eco { left: 75px; }
  .benefit.sustain { left: 249px; }
  .benefit.reuse { left: 418px; }
</style>
</head>
<body>
<div class="package-front">
  <div class="bamboo-right" role="img" aria-label="Bamboo stalks and leaves line drawing"></div>
  <div class="bamboo-left" role="img" aria-label="Bamboo stalks and leaves line drawing"></div>

  <div class="brand-block">
    <span class="brand-name">BRIMO<br>TALVE</span>
  </div>

  <h1 class="product-title main">REUSABLE</h1>
  <h2 class="product-title sub">CLEANING PADS</h2>

  <div class="content-box">
    <div class="mesh-bag" role="img" aria-label="Cotton mesh bag filled with pads"></div>
    <ul class="content-list">
      <li>70% Bamboo</li>
      <li>30% Cotton</li>
      <li class="wide">100% Cotton mesh bag</li>
    </ul>
  </div>

  <svg class="count-badge" viewBox="0 0 116 116">
    <polygon fill="var(--leaf-green)" points="58,0 66,14 81,5 84,22 101,18 97,35 114,38 104,52 116,62 101,70 108,86 91,87 90,104 75,98 66,114 58,101 48,114 41,98 25,104 25,87 8,86 15,70 0,62 12,52 2,38 19,35 15,18 32,22 36,5 50,14"/>
    <text x="58" y="64" text-anchor="middle" fill="var(--white)" font-family="Poppins, sans-serif" font-weight="700" font-size="34">24</text>
    <text x="58" y="84" text-anchor="middle" fill="var(--white)" font-family="Poppins, sans-serif" font-weight="700" font-size="13">PADS</text>
  </svg>

  <div class="benefits">
    <div class="benefit eco">
      <svg width="58" height="58" viewBox="0 0 58 58"><circle cx="29" cy="29" r="28" fill="var(--leaf-green)"/><circle cx="29" cy="29" r="14" fill="none" stroke="var(--kraft)" stroke-width="4"/></svg>
      Eco Friendly
    </div>
    <div class="benefit sustain">
      <svg width="58" height="58" viewBox="0 0 58 58"><circle cx="29" cy="29" r="28" fill="var(--leaf-green)"/><path d="M18 38 C18 24 30 16 42 16 C42 30 32 38 18 38 Z" fill="var(--kraft)"/></svg>
      Sustainable
    </div>
    <div class="benefit reuse">
      <svg width="58" height="58" viewBox="0 0 58 58"><circle cx="29" cy="29" r="28" fill="var(--leaf-green)"/><path d="M29 14 L42 38 L16 38 Z" fill="none" stroke="var(--kraft)" stroke-width="4" stroke-linejoin="round"/></svg>
      Reusable
    </div>
  </div>
</div>
</body>
</html>
```